Larkwood Trade Fair Invite October 2014

Require an oversized postcard utilizing my files/photos. This invitation will be sent to my company's existing and target account base inviting them to view/purchase our new furniture product introductions.
Updates

Emailed my files to ArtFolio to upload them to this project. Was unable to upload them myself. On the front of the postcard, I would like to see the photo that is included in the upload. It's a photo of a covered sofa sitting in a warehouse backdrop. The text copy for this front side of postcard is to read: Brendle Furniture is about to uncover the next big thing in quality and style! Soon we'll be introducing beautiful styles that make a statement. Visit Brendle at Larkwood Trade Fair as we are about to uncover the next best thing in leather - TQV - Truly Quiet Velvet collection! Text Copy for the back of the post card is to read: Find us at The Granary Hall 482 E. Juniper Avenue High Point, NC (Showroom Entrance adjacent to the Clocktower Block on Juniper Avenue) October 18-23, 2014 See Our Other New Furniture Collections Halden Elm Row Ransome Take Advantage of our Market Specials Instant Rebates Special Market Credit Terms Special Market Discounts Brendle Furniture 260 N. Alder Lane Brendle, WI 58312 p 608-924-3057 f 608-924-3058 www.brendlefurnishings.example Like us on Friendwall (use logo) Pin us on Clipboardia (use logo)

Target Market(s)

Our target audience are retailers who sell custom upholstery furniture.

Industry/Entity Type

It Company

Font styles to use
Other font styles liked:
• Century Gothic

Requirements
Must have
• Company logo; clear message, clean design

```html
<!DOCTYPE html>
<html lang="en">
<head>
<meta charset="utf-8">
<title>Brendle Furniture – Postcard</title>
<link href="https://fonts.googleapis.com/css2?family=Questrial&family=Montserrat:wght@700&display=swap" rel="stylesheet">
<style>
  :root {
    --stage: #1f1f1f;
    --red: #8f1b21;
    --red-light: #a8262d;
    --taupe: #b3a79b;
    --sand: #d9cfc4;
    --cream: #f3ede7;
    --panel-top: #f1ece7;
    --panel-bottom: #c8bcb1;
    --ink: #2e2a28;
    --photo-wall: #a8553f;
    --photo-floor: #d9a95a;
    --rule: #8a8480;
  }
  * { box-sizing: border-box; margin: 0; padding: 0; }
  html, body { width: 797px; height: 1200px; overflow: hidden; background: var(--stage); }
  body { position: relative; font-family: "Questrial", "Century Gothic", sans-serif; }

  .card { position: absolute; left: 40px; width: 717px; overflow: hidden; }
  .card-front { top: 40px; height: 500px; background: var(--red); }
  .card-back { top: 615px; height: 465px; background: #fff; }
  .card svg.shapes { position: absolute; inset: 0; }

  /* front */
  .tagline-word { position: absolute; top: 78px; color: var(--cream); font-size: 19px; letter-spacing: 1.5px; }
  .tagline-word.left { left: 172px; }
  .tagline-word.right { left: 412px; }
  .brand-box {
    position: absolute; left: 310px; top: 52px; width: 86px; height: 84px;
    background: #fff; border: 2px solid var(--sand);
    display: flex; align-items: center; justify-content: center;
  }
  .brand-name { color: var(--red); font-size: 17px; }
  .front-title {
    position: absolute; right: 12px; top: 418px;
    color: var(--sand); font-family: "Montserrat", sans-serif; font-weight: 700; font-size: 25px;
  }
  .front-line {
    position: absolute; left: 32px; top: 452px;
    color: var(--cream); font-size: 27px; white-space: nowrap;
  }

  /* back */
  .strip-word {
    position: absolute; color: var(--cream); font-size: 13px; letter-spacing: 1.5px;
    transform: rotate(-90deg); transform-origin: left top; white-space: nowrap;
  }
  .strip-word.upper { left: 34px; top: 188px; }
  .strip-word.lower { left: 34px; top: 345px; }
  .strip-brand {
    position: absolute; left: 22px; top: 195px; width: 40px; height: 54px;
    background: #fff; display: flex; align-items: center; justify-content: center;
  }
  .strip-brand span { color: var(--red); font-size: 11px; transform: rotate(-90deg); }

  .contact { position: absolute; left: 80px; top: 0; width: 315px; height: 465px; text-align: center; color: var(--ink); }
  .contact h2 {
    font-family: "Montserrat", sans-serif; font-weight: 700; color: var(--red);
    font-size: 31px; letter-spacing: 0.5px;
  }
  .contact .heading-contact { margin-top: 28px; }
  .contact .address { font-size: 16px; line-height: 20px; margin-top: 12px; }
  .contact .address + .address { margin-top: 22px; }
  .contact .line { font-size: 16px; margin-top: 22px; display: flex; align-items: center; justify-content: center; gap: 6px; }
  .contact .heading-follow { margin-top: 22px; }
  .icon { display: inline-block; vertical-align: -2px; }
  .socials { display: flex; justify-content: center; gap: 14px; margin-top: 14px; font-size: 12px; }
  .social { display: flex; align-items: center; gap: 5px; }
  .social .dot { width: 20px; height: 20px; border-radius: 50%; }
  .social.friendwall .dot { background: #3b5a9a; }
  .social.clipboardia .dot { background: #c8232c; }

  .stamp-box { position: absolute; left: 646px; top: 22px; width: 58px; height: 68px; border: 1px solid #555; }
  .address-rule { position: absolute; left: 447px; width: 258px; height: 1px; background: var(--rule); }
  .faint-brand {
    position: absolute; left: 498px; top: 240px; width: 160px; text-align: center;
    color: #e9e6e3; font-size: 28px;
  }
</style>
</head>
<body>

<section class="card card-front">
  <svg class="shapes" width="717" height="500" viewBox="0 0 717 500">
    <defs>
      <linearGradient id="photo-tone" x1="0" y1="0" x2="0" y2="1">
        <stop offset="0" stop-color="var(--photo-wall)"/>
        <stop offset="0.45" stop-color="#b06a4c"/>
        <stop offset="0.55" stop-color="var(--photo-floor)"/>
        <stop offset="1" stop-color="#e6b868"/>
      </linearGradient>
    </defs>
    <rect class="band" x="0" y="66" width="717" height="54" fill="var(--taupe)"/>
    <polygon class="photo" role="img" aria-label="Photo of a sofa under a white sheet in a brick warehouse with a wooden floor"
      points="0,158 282,158 378,186 474,158 717,158 717,385 480,385 440,405 0,405" fill="url(#photo-tone)"/>
    <polyline points="0,152 280,152 378,181 476,152 717,152" fill="none" stroke="var(--cream)" stroke-width="2"/>
    <polyline points="0,412 442,412 482,392 717,392" fill="none" stroke="var(--cream)" stroke-width="2"/>
  </svg>
  <span class="tagline-word left">handcrafted</span>
  <span class="tagline-word right">upholstery</span>
  <div class="brand-box"><span class="brand-name">Brendle</span></div>
  <h1 class="front-title">Brendle Furniture</h1>
  <p class="front-line">is about to uncover the next big thing in leather</p>
</section>

<section class="card card-back">
  <svg class="shapes" width="717" height="465" viewBox="0 0 717 465">
    <defs>
      <linearGradient id="panel-tone" x1="0" y1="0" x2="1" y2="1">
        <stop offset="0" stop-color="var(--panel-top)"/>
        <stop offset="1" stop-color="var(--panel-bottom)"/>
      </linearGradient>
    </defs>
    <rect x="80" y="0" width="315" height="465" fill="url(#panel-tone)"/>
    <polygon points="0,0 80,0 80,180 112,215 80,250 80,465 0,465" fill="var(--red)"/>
    <polyline points="86,0 86,178 120,215 86,252 86,465" fill="none" stroke="var(--cream)" stroke-width="2"/>
    <rect x="22" y="0" width="38" height="465" fill="var(--taupe)"/>
  </svg>
  <span class="strip-word upper">upholstery</span>
  <div class="strip-brand"><span>Brendle</span></div>
  <span class="strip-word lower">handcrafted</span>

  <div class="contact">
    <h2 class="heading-contact">CONTACT US</h2>
    <p class="address">
      <svg class="icon" width="14" height="13" viewBox="0 0 14 13"><path d="M7 0 0 6h2v7h4V9h2v4h4V6h2z" fill="var(--red)"/></svg>
      Brendle Furniture<br>260 N. Alder Lane Brendle,<br>WI 58312
    </p>
    <p class="address">
      <svg class="icon" width="14" height="13" viewBox="0 0 14 13"><path d="M7 0 0 6h2v7h4V9h2v4h4V6h2z" fill="var(--red)"/></svg>
      The Granary Hall<br>482 E. Juniper Avenue High<br>Point, NC
    </p>
    <p class="line">
      <svg class="icon" width="13" height="13" viewBox="0 0 13 13"><path d="M3 0 5 3 3.5 4.5c1 2 3 4 5 5L10 8l3 2-1.5 3C6 12 1 7 0 1.5z" fill="var(--red)"/></svg>
      608-924-3057
    </p>
    <p class="line">
      <svg class="icon" width="15" height="13" viewBox="0 0 15 13"><rect x="0" y="4" width="15" height="9" rx="1" fill="var(--red)"/><rect x="3" y="0" width="9" height="5" fill="var(--red)"/><rect x="3" y="7" width="9" height="3" fill="#fff"/></svg>
      608-924-3058
    </p>
    <p class="line">
      <svg class="icon" width="13" height="13" viewBox="0 0 13 13"><circle cx="6.5" cy="6.5" r="6" fill="none" stroke="var(--red)" stroke-width="1.4"/><path d="M0.5 6.5h12M6.5 0.5c-3 3-3 9 0 12M6.5 0.5c3 3 3 9 0 12" fill="none" stroke="var(--red)" stroke-width="1"/></svg>
      www.brendlefurnishings.example
    </p>
    <h2 class="heading-follow">FOLLOW US</h2>
    <div class="socials">
      <span class="social friendwall"><span class="dot"></span>Friendwall</span>
      <span class="social clipboardia"><span class="dot"></span>Clipboardia</span>
    </div>
  </div>

  <div class="stamp-box"></div>
  <div class="faint-brand">Brendle</div>
  <div class="address-rule" style="top:203px"></div>
  <div class="address-rule" style="top:260px"></div>
  <div class="address-rule" style="top:318px"></div>
</section>

</body>
</html>
```